Mondaxe custom business card design

Need a authentic, innovative business card design for a new mobile app business. I am uploading a few screen images from our app for you to view. I would like app design theme to match business card design. I can also send logo images.

```html
<!DOCTYPE html>
<html lang="en">
<head>
<meta charset="utf-8">
<title>Mondaxe business card</title>
<link href="https://fonts.googleapis.com/css2?family=Montserrat:wght@400;500;700;800;900&display=swap" rel="stylesheet">
<style>
  :root {
    --backdrop: #22084f;
    --card: #f7f7f5;
    --ink: #0d0d0d;
    --brand-purple: #5b1e9c;
    --brand-black: #111111;
  }
  * { margin: 0; padding: 0; box-sizing: border-box; }
  html, body {
    width: 1200px;
    height: 863px;
    overflow: hidden;
    background: var(--backdrop);
    font-family: "Montserrat", Arial, sans-serif;
    color: var(--ink);
  }
  .card-pair {
    position: absolute;
    top: 160px;
    left: 0;
    width: 1200px;
    display: flex;
    justify-content: center;
    gap: 80px;
  }
  .card {
    position: relative;
    width: 320px;
    height: 540px;
    background: var(--card);
    overflow: hidden;
  }

  /* Front */
  .front-artwork {
    position: absolute;
    inset: 0;
    width: 320px;
    height: 540px;
    display: block;
  }
  .front-name {
    position: absolute;
    right: 18px;
    bottom: 22px;
    font-weight: 900;
    font-size: 56px;
    letter-spacing: 1px;
    writing-mode: vertical-rl;
    transform: rotate(180deg);
    line-height: 1;
    color: var(--ink);
  }

  /* Back */
  .back {
    display: flex;
    flex-direction: column;
    align-items: center;
    text-align: center;
  }
  .brand-dot {
    margin-top: 78px;
    width: 74px;
    height: 74px;
    border-radius: 50%;
    background: var(--brand-purple);
  }
  .brand-name {
    margin-top: 10px;
    font-weight: 800;
    font-size: 31px;
    line-height: 1.1;
  }
  .person-name {
    margin-top: 46px;
    font-weight: 800;
    font-size: 20px;
    letter-spacing: 0.5px;
    line-height: 1.2;
  }
  .person-role {
    font-weight: 500;
    font-size: 18px;
    line-height: 1.2;
  }
  .contact-list {
    list-style: none;
    margin-top: 34px;
    font-size: 15px;
    line-height: 1.4;
  }
  .address {
    margin-top: 24px;
    font-style: normal;
    font-size: 15px;
    line-height: 1.4;
  }
</style>
</head>
<body>
  <main class="card-pair">
    <section class="card front" aria-label="Card front">
      <svg class="front-artwork" viewBox="0 0 320 540" role="img" aria-label="Bold black and purple brand graphic filling the card front">
        <defs>
          <linearGradient id="front-fill" x1="0" y1="0" x2="0.6" y2="1">
            <stop offset="0" stop-color="#111111"/>
            <stop offset="0.45" stop-color="#2a0f4d"/>
            <stop offset="1" stop-color="#5b1e9c"/>
          </linearGradient>
        </defs>
        <path d="M0 60 C 90 40, 150 0, 180 0 H320 V150 C 320 290, 220 330, 222 440 V540 H0 Z" fill="url(#front-fill)"/>
      </svg>
      <p class="front-name">Mondaxe</p>
    </section>

    <section class="card back" aria-label="Card back">
      <div class="brand-dot"></div>
      <p class="brand-name">Mondaxe</p>
      <h1 class="person-name">MARCUS HALE</h1>
      <p class="person-role">Manager</p>
      <ul class="contact-list">
        <li>012 555 0147</li>
        <li>email@mondaxe.com</li>
        <li>www.mondaxe.com</li>
      </ul>
      <address class="address">418 Lakeview Avenue<br>Macon, GA, Georgia, 31201</address>
    </section>
  </main>
</body>
</html>
```